International Wine events organiser seeks simple but stunning business card

I am a freelance events, marketing and PR provider specialised in the Wine industry. I help wineries and wine regions reach trade and consumers in foreign markets through events, help with the websites and communications, press trips and promotional activities. I am looking for a business card which is simple yet effective and is linked to events and communication.

I work mainly - but exclusively - with Italian wineries organising events for them in foreign market.s

I would like to use red in the logo as my present website (lenamorvick.com) used grey and red (although I will be changing the design at a later date).

Target Market(s)

Wine producers, promotional bodies in wine sector, companies looking to hire event organisers,

Industry/Entity Type

Marketing

Requirements
Must have
• My Name - Lena Morvick
My address
My phone
My website : www.lenamorvick.com
my Blog : velvetandtone.me

Should not have
• Butterflies, stars, flowers, anything not particularly linked to wine - would like to keep it simple, modern and eye-catching without being too cliche.

```html
<!DOCTYPE html>
<html lang="en">
<head>
<meta charset="utf-8">
<title>Lena Morvick – Business Card</title>
<link href="https://fonts.googleapis.com/css2?family=EB+Garamond:wght@400&display=swap" rel="stylesheet">
<style>
  :root {
    --card-bg: #ffffff;
    --accent-red: #ec2227;
    --slate-grey: #6d7879;
    --ornament-grey: #8f9a9a;
    --ornament-red: #ec2227;
  }
  * { margin: 0; padding: 0; box-sizing: border-box; }
  html, body {
    width: 667px;
    height: 1200px;
    overflow: hidden;
    background: var(--card-bg);
  }
  .card {
    position: relative;
    width: 667px;
    height: 1200px;
    background: var(--card-bg);
    font-family: "EB Garamond", Garamond, "Times New Roman", serif;
    overflow: hidden;
  }
  .ornament {
    position: absolute;
  }
  .ornament--top {
    left: 55px;
    top: 0;
    width: 612px;
    height: 248px;
    border-radius: 0 0 40% 60% / 0 0 70% 60%;
    background: radial-gradient(ellipse at 55% 35%, var(--ornament-grey) 0%, rgba(143,154,154,0.55) 45%, rgba(143,154,154,0) 75%);
  }
  .ornament--side {
    left: 0;
    top: 564px;
    width: 285px;
    height: 420px;
    border-radius: 0 60% 55% 0 / 0 50% 50% 0;
    background: radial-gradient(ellipse at 20% 45%, var(--ornament-red) 0%, rgba(236,34,39,0.55) 45%, rgba(236,34,39,0) 75%);
  }
  .name {
    position: absolute;
    top: 270px;
    left: 0;
    width: 100%;
    text-align: center;
    font-size: 88px;
    font-weight: 400;
    color: var(--accent-red);
    letter-spacing: 1px;
    line-height: 1;
  }
  .tagline {
    position: absolute;
    top: 406px;
    left: 0;
    width: 100%;
    text-align: center;
    font-size: 39px;
    line-height: 58px;
    color: var(--slate-grey);
  }
  .contact {
    position: absolute;
    top: 1024px;
    left: 0;
    width: 100%;
    text-align: center;
    font-size: 35px;
    line-height: 48px;
    color: var(--slate-grey);
  }
  .contact__label {
    color: var(--accent-red);
  }
</style>
</head>
<body>
  <div class="card">
    <div class="ornament ornament--top" role="img" aria-label="Grey calligraphic swirl ornament"></div>
    <div class="ornament ornament--side" role="img" aria-label="Red calligraphic swirl ornament"></div>

    <h1 class="name">Lena Morvick</h1>
    <p class="tagline">Comunication and events<br>for the world wine</p>

    <div class="contact">
      <p class="contact__line"><span class="contact__label">Tel:</span> +49 170 5832 614</p>
      <p class="contact__line"><span class="contact__label">mail:</span>lena@lenamorvick.com</p>
    </div>
  </div>
</body>
</html>
```